Calder Ridge Minerals

Looking for a cool, glossy business card...white with our logo on one side and then the a smaller version of the logo on the other side (top left hand corner) and then the name and position of the person next to it, and then the office address and email address on the bottom left hand corner and the phone numbers & email address on the bottom right hand corner. I have the logo already...can pass it on when you're ready.

```html
<!DOCTYPE html>
<html lang="en">
<head>
<meta charset="utf-8">
<title>Calder Ridge Minerals – Business Card</title>
<link rel="stylesheet" href="https://fonts.googleapis.com/css2?family=Cinzel:wght@500;600&family=Lato:wght@400&display=swap">
<style>
  :root {
    --backdrop: #c9c9cb;
    --card: #fbfbfb;
    --ink: #3a3a3a;
    --ink-soft: #555;
    --blue: #2a2ec9;
    --red: #b2141f;
    --icon: #5b3fa8;
  }
  * { margin: 0; padding: 0; box-sizing: border-box; }
  html, body { width: 1200px; height: 852px; overflow: hidden; }
  body {
    background: var(--backdrop);
    font-family: "Lato", sans-serif;
    color: var(--ink);
    position: relative;
  }
  .card {
    position: absolute;
    top: 277px;
    width: 520px;
    height: 298px;
    background: var(--card);
    border-radius: 14px;
    overflow: hidden;
  }
  .card--front { left: 50px; }
  .card--back { left: 630px; }

  .brand-name {
    font-family: "Cinzel", serif;
    font-weight: 600;
    color: var(--ink);
    letter-spacing: 1px;
    display: flex;
    align-items: center;
    gap: 10px;
  }
  .brand-mark {
    width: 14px; height: 14px;
    background: var(--blue);
    flex: none;
  }

  /* Front */
  .front-brand {
    position: absolute;
    left: 0; right: 0; top: 96px;
    display: flex;
    justify-content: center;
  }
  .front-brand .brand-name { font-size: 30px; }
  .front-web {
    position: absolute;
    left: 0; right: 0; top: 200px;
    text-align: center;
    font-size: 14px;
    color: var(--ink-soft);
  }
  .front-rule {
    position: absolute;
    top: 226px;
    height: 2px;
    width: 52px;
  }
  .front-rule--blue { left: 130px; background: var(--blue); }
  .front-rule--red { right: 130px; background: var(--red); }
  .front-band {
    position: absolute;
    left: 0; right: 0; bottom: 0;
    height: 12px;
    display: flex;
  }
  .front-band span { flex: 1; }
  .front-band .band-blue { background: var(--blue); }
  .front-band .band-red { background: var(--red); }

  /* Back */
  .back-brand {
    position: absolute;
    left: 30px; top: 150px;
    width: 200px;
  }
  .back-brand .brand-name {
    font-size: 20px;
    line-height: 1.2;
    gap: 8px;
  }
  .back-brand .brand-mark { width: 10px; height: 10px; }
  .person {
    position: absolute;
    left: 270px; top: 82px;
  }
  .person-name {
    font-family: "Cinzel", serif;
    font-weight: 600;
    font-size: 20px;
    color: var(--blue);
  }
  .person-role {
    font-size: 12px;
    color: var(--ink-soft);
    margin-top: 2px;
  }
  .contacts {
    list-style: none;
    margin-top: 16px;
  }
  .contacts li {
    display: flex;
    align-items: center;
    gap: 9px;
    font-size: 12px;
    color: var(--ink);
    line-height: 20px;
    white-space: nowrap;
  }
  .contacts svg { width: 11px; height: 11px; flex: none; }
</style>
</head>
<body>

<section class="card card--front" aria-label="Card front">
  <div class="front-brand">
    <span class="brand-name"><i class="brand-mark"></i>Calder Ridge Minerals</span>
  </div>
  <p class="front-web">www.calderridgeminerals.com</p>
  <div class="front-rule front-rule--blue"></div>
  <div class="front-rule front-rule--red"></div>
  <div class="front-band"><span class="band-blue"></span><span class="band-red"></span></div>
</section>

<section class="card card--back" aria-label="Card back">
  <div class="back-brand">
    <span class="brand-name"><i class="brand-mark"></i><span>Calder Ridge<br>Minerals</span></span>
  </div>
  <div class="person">
    <h1 class="person-name">Dale R Whitman</h1>
    <p class="person-role">Managing Director</p>
    <ul class="contacts">
      <li>
        <svg viewBox="0 0 12 12" aria-hidden="true"><rect width="12" height="12" rx="2" fill="var(--icon)"/><path d="M3.5 3h1.5l.6 1.6-.9.7a4.5 4.5 0 0 0 2 2l.7-.9 1.6.6V8.5A1 1 0 0 1 8 9.3 5.6 5.6 0 0 1 2.7 4 1 1 0 0 1 3.5 3z" fill="#fff"/></svg>
        (555) 014-2290
      </li>
      <li>
        <svg viewBox="0 0 12 12" aria-hidden="true"><rect width="12" height="12" rx="2" fill="var(--icon)"/><rect x="2.5" y="3.5" width="7" height="5" fill="none" stroke="#fff"/><path d="M2.5 3.5 6 6.3l3.5-2.8" fill="none" stroke="#fff"/></svg>
        info@calderridgeminerals.com
      </li>
      <li>
        <svg viewBox="0 0 12 12" aria-hidden="true"><circle cx="6" cy="6" r="6" fill="var(--icon)"/><circle cx="6" cy="6" r="3.6" fill="none" stroke="#fff" stroke-width=".8"/><path d="M2.4 6h7.2M6 2.4c-1.6 2-1.6 5.2 0 7.2M6 2.4c1.6 2 1.6 5.2 0 7.2" fill="none" stroke="#fff" stroke-width=".7"/></svg>
        www.calderridgeminerals.com
      </li>
      <li>
        <svg viewBox="0 0 12 12" aria-hidden="true"><circle cx="6" cy="6" r="6" fill="var(--icon)"/><path d="M6 2.5a2.3 2.3 0 0 1 2.3 2.3C8.3 6.6 6 9.5 6 9.5S3.7 6.6 3.7 4.8A2.3 2.3 0 0 1 6 2.5z" fill="#fff"/><circle cx="6" cy="4.8" r=".9" fill="var(--icon)"/></svg>
        41 Harlow Lane Mesa Bend, TX 75012
      </li>
    </ul>
  </div>
</section>

</body>
</html>
```